Tolvi Camp - Masai Mara

We need a website for our wilderness camp in the Masai Mara.
We want a website with the following information

Modern design, but easy to navigate
International with multiple languages. Norwegian, Polish, English.
Customers are people with an interest in the outdoors, photography, animals and culture.
Page with lots of pictures
Information about owners of Tolvi Camp
Information about Tolvi Camp
Maasai Mara. Where is it and what is it known for. Map with mark where the match is.
Package tour offer. Min 3 pcs.
Miscellaneous add. Diani Beach, Balloon ride, Night safari, walking safari, etc
Info about ambassadors that Tolvi camp has around the world. (Sellers)
Image archive and film archive
The weather in Mara now. The weather in Mara all year round
Feedback from customers
Logos from partners
Contact information
Link to Facbook, Instagram, TikTok, Youtube
Signing up for newsletters

If there are other smart things to bring, make suggestions.
The page must be able to be updated by us with text and images.

The domain is tolvicamp.com and tolvicamp.no

This is a page I like https://kebrato.com/

```html
<!DOCTYPE html>
<html lang="en">
<head>
<meta charset="utf-8">
<title>Tolvi Camp - Masai Mara</title>
<link rel="stylesheet" href="https://fonts.googleapis.com/css2?family=Alfa+Slab+One&family=Playfair+Display:wght@400;700&family=Roboto:wght@300;400;500;700&family=Roboto+Condensed:wght@400;700&display=swap">
<style>
:root{
  --ink:#222;
  --muted:#555;
  --light-bg:#f3f4f7;
  --white:#fff;
  --accent:#f5a623;
  --red:#e3101a;
  --blue:#1b8fd6;
  --gold:#f5c518;
}
*{margin:0;padding:0;box-sizing:border-box}
html,body{width:1200px;height:5164px;overflow:hidden}
body{position:relative;font-family:"Roboto",sans-serif;color:var(--ink);background:var(--light-bg)}
.abs{position:absolute}
.photo{position:absolute}

/* hero */
.hero{left:0;top:0;width:1200px;height:760px;
  background:
    radial-gradient(ellipse 260px 200px at 720px 330px,rgba(238,238,232,.75) 0%,rgba(200,196,186,.35) 45%,rgba(0,0,0,0) 75%),
    radial-gradient(ellipse 360px 220px at 520px 430px,rgba(122,70,38,.85) 0%,rgba(98,58,34,.5) 50%,rgba(0,0,0,0) 80%),
    radial-gradient(ellipse 220px 120px at 820px 240px,rgba(90,84,80,.7) 0%,rgba(0,0,0,0) 80%),
    radial-gradient(ellipse 700px 220px at 500px 640px,rgba(110,122,92,.75) 0%,rgba(0,0,0,0) 75%),
    radial-gradient(ellipse at 20% 30%,#5a5e4a 0%,rgba(0,0,0,0) 50%),
    radial-gradient(ellipse at 90% 70%,#6a6e58 0%,rgba(0,0,0,0) 55%),
    linear-gradient(180deg,#3a3d2e 0%,#4c5040 50%,#5d6350 100%)}
.hero-wave{left:0;top:660px;width:1200px;height:110px}
.brand{display:flex;align-items:center;gap:8px;color:var(--white);font-family:"Alfa Slab One",serif;font-size:15px}
.brand .dot{width:34px;height:34px;border-radius:50%;border:2px solid var(--white)}
.nav{left:430px;top:34px;display:flex;gap:17px;font-family:"Alfa Slab One",serif;font-size:11px;letter-spacing:1px;color:var(--white)}
.nav .flag{width:16px;height:16px;border-radius:50%;background:#c8102e;border:2px solid var(--white);margin-top:-2px}
.play{left:566px;top:302px;width:68px;height:68px;border-radius:50%;background:rgba(255,255,255,.35);display:flex;align-items:center;justify-content:center}
.play span{width:46px;height:46px;border-radius:50%;background:var(--white);display:flex;align-items:center;justify-content:center}

/* about */
.about-label{left:148px;top:904px;font-family:"Roboto Condensed",sans-serif;font-weight:700;font-size:14px;color:#333}
.about-title{left:148px;top:924px;font-family:"Roboto Condensed",sans-serif;font-weight:700;font-size:26px;color:var(--ink)}
.about-text{left:148px;width:530px;font-size:12.5px;line-height:20px;color:var(--muted)}
.sign{left:148px;top:1208px;display:flex;align-items:center;gap:8px;font-size:11px;color:var(--muted)}
.sign .mark{width:124px;height:26px;background:linear-gradient(90deg,#e3e4e8,#eceef1)}
.btn-dark{background:#111;color:var(--white);font-size:11px;font-weight:700;letter-spacing:.5px;display:flex;align-items:center;justify-content:center}
.polaroid{position:absolute;background:var(--white);box-shadow:0 4px 14px rgba(0,0,0,.18);padding:12px}
.polaroid div{width:100%;height:100%}
.tape{position:absolute;width:56px;height:12px;background:rgba(200,200,200,.8)}

/* framed bands */
.band{left:0;width:1200px}
.frame{position:absolute;left:202px;width:816px;border:1px solid rgba(255,255,255,.55)}
.band-title{font-family:"Alfa Slab One",serif;font-size:32px;color:var(--white)}
.band-sub{font-size:10px;font-weight:700;letter-spacing:2px;color:var(--white)}
.band-text{width:680px;font-size:12.5px;line-height:17px;color:#eee}
.band-link{font-size:10px;font-weight:700;letter-spacing:1.5px;color:var(--white)}
.band-link b{color:var(--accent)}
.corner-mark{display:flex;flex-direction:column;align-items:center;gap:4px;color:var(--white);font-weight:700;font-size:11px}
.corner-mark .c{width:60px;height:60px;border-radius:50%;background:rgba(255,255,255,.85)}

/* section heads */
.sec-mark{left:560px;width:80px;display:flex;flex-direction:column;align-items:center;gap:4px;font-weight:700;font-size:11px;color:#555}
.sec-mark .c{width:64px;height:64px;border-radius:50%;background:linear-gradient(#cfcfcf,#8a8a8a)}
.sec-title{left:0;width:1200px;text-align:center;font-family:"Playfair Display",serif;font-size:37px;color:var(--ink)}
.sec-sub{left:0;width:1200px;text-align:center;font-size:12px;letter-spacing:4px;color:#333}

/* destinations */
.tile{position:absolute;width:200px;height:244px;overflow:hidden}
.tile .pic{height:100%}
.tile .cap{position:absolute;left:0;bottom:0;width:100%;height:44px;background:rgba(0,0,0,.45);color:var(--white);text-align:center;padding-top:9px}
.tile .cap p{font-size:11px}
.tile .cap small{display:block;font-size:8px;letter-spacing:2px;margin-top:3px}

/* highlights */
.hl-title{left:0;width:1200px;text-align:center;font-weight:300;font-size:38px;color:var(--white)}
.hl-sub{left:0;width:1200px;text-align:center;font-size:14px;letter-spacing:5px;color:var(--white)}
.ring{left:568px;top:2822px;width:60px;height:60px;border-radius:50%;border:3px solid var(--white);display:flex;align-items:center;justify-content:center}

/* packages */
.pkg-title{left:0;width:1200px;text-align:center;font-family:"Playfair Display",serif;font-size:36px;letter-spacing:1px;color:var(--ink)}
.card{position:absolute;top:3218px;width:280px;height:512px;background:var(--white);box-shadow:0 2px 10px rgba(0,0,0,.12)}
.card .img{position:absolute;left:8px;top:8px;width:264px;height:322px}
.card h3{position:absolute;top:356px;width:100%;text-align:center;font-size:12px;font-weight:400;color:#222}
.card p{position:absolute;top:376px;left:22px;width:236px;text-align:center;font-size:10.5px;line-height:15px;color:#777}
.card .meta{position:absolute;top:418px;width:100%;text-align:center;font-size:11px;color:#333}
.card .btn-dark{position:absolute;top:462px;left:88px;width:104px;height:28px;font-size:10px}

/* partners */
.partner-title{left:0;top:4354px;width:1200px;text-align:center;font-family:"Alfa Slab One",serif;font-size:27px;letter-spacing:2px;color:#222}
.partner{position:absolute;top:4420px;width:168px;height:100px;background:var(--white);box-shadow:0 1px 6px rgba(0,0,0,.1);display:flex;align-items:center;justify-content:center;font-weight:700;font-size:15px;color:#2a6fb0}

/* footer */
.footer{left:0;top:4620px;width:1200px;height:544px;
  background:
    radial-gradient(ellipse 260px 140px at 600px 4820px,rgba(0,0,0,0) 0%,rgba(0,0,0,0) 100%),
    radial-gradient(ellipse 420px 120px at 560px 400px,rgba(255,190,80,.85) 0%,rgba(230,120,40,.5) 45%,rgba(0,0,0,0) 80%),
    linear-gradient(180deg,#2a180d 0%,#3e2212 30%,#7a3a14 55%,#c0601e 68%,#8a4418 78%,#2e190c 88%,#140a05 100%)}
.f-small{font-size:10px;letter-spacing:1.5px;color:var(--white)}
.f-big{font-size:20px;letter-spacing:2px;color:var(--white)}
.f-links{left:516px;top:4910px;font-size:9.5px;letter-spacing:1px;color:var(--white);line-height:21px}
.f-info{left:756px;font-size:11.5px;color:var(--white)}
.social{left:756px;top:4956px;display:flex;gap:14px}
.social span{width:20px;height:20px;border-radius:50%;background:var(--white)}
.copy{left:0;top:5100px;width:1200px;text-align:center;font-size:11px;color:var(--white)}
</style>
</head>
<body>

<!-- HERO -->
<div class="photo hero" role="img" aria-label="Close-up of a coucal bird perched on a thorny acacia branch"></div>
<svg class="abs hero-wave" viewBox="0 0 1200 110" preserveAspectRatio="none"><path d="M0 60 C 200 10, 380 100, 620 70 S 1000 20, 1200 40 L1200 110 L0 110Z" fill="#f3f4f7"/></svg>
<div class="abs brand" style="left:176px;top:38px"><span class="dot"></span>Tolvi Camp</div>
<nav class="abs nav"><span>HOME</span><span>ACTIVITIES</span><span>ACCOMMODATION</span><span>ITINERARIES</span><span>GALLERIES</span><span>MORE INFO</span><span class="flag"></span></nav>
<div class="abs play"><span><svg width="14" height="16"><path d="M2 1 L13 8 L2 15Z" fill="#1b5fd6"/></svg></span></div>

<!-- ABOUT -->
<div class="abs about-label">About Maasai Mara</div>
<h1 class="abs about-title">WELCOME TO Tolvi Camp</h1>
<p class="abs about-text" style="top:970px">It is a long established fact that a reader will be distracted by the readable content of a page when looking at its layout. The point of using Lorem Ipsum is that it has a more-or-less normal distribution of letters, as opposed to using 'Content here, content here', making it look like readable English. Many desktop publishing packages and web page editors now use Lorem Ipsum as their default model text, and a search for 'lorem ipsum' will uncover many web sites still in their infancy.</p>
<p class="abs about-text" style="top:1130px">To take a trivial example, which of us ever undertakes laborious physical exercise, except to obtain some advantage from it? But who has any right to find fault with a man who chooses to enjoy a pleasure that has no annoying consequences</p>
<div class="abs sign"><span class="mark" role="img" aria-label="Handwritten signature of Ingrid M. Solberg"></span>(owners)</div>
<div class="abs btn-dark" style="left:148px;top:1266px;width:122px;height:32px">LEARN MORE</div>

<div class="polaroid" style="left:738px;top:886px;width:232px;height:260px"><div role="img" aria-label="Lion walking through tall grass" style="background:radial-gradient(ellipse 70px 90px at 50% 40%,#9a7448 0%,#6a4e30 50%,rgba(0,0,0,0) 85%),linear-gradient(180deg,#3a3026,#2a2218 60%,#4a4030)"></div></div>
<div class="tape" style="left:818px;top:880px"></div>
<div class="polaroid" style="left:964px;top:880px;width:146px;height:190px"><div role="img" aria-label="Malachite kingfisher on a branch" style="background:radial-gradient(ellipse 30px 40px at 50% 45%,#d86a2a 0%,#2a6fb0 45%,rgba(0,0,0,0) 80%),linear-gradient(180deg,#7a8a6a,#3a4a30)"></div></div>
<div class="tape" style="left:1012px;top:874px"></div>
<div class="polaroid" style="left:866px;top:1078px;width:184px;height:218px"><div role="img" aria-label="Maasai warrior silhouetted at sunset" style="background:radial-gradient(ellipse 80px 40px at 50% 55%,#f4b048 0%,#d8742a 40%,rgba(0,0,0,0) 80%),linear-gradient(180deg,#3a2a22 0%,#b85a22 45%,#3a1e0e 70%,#120a06)"></div></div>
<div class="tape" style="left:1010px;top:1280px;transform:rotate(-35deg)"></div>
<div class="tape" style="left:848px;top:1088px;transform:rotate(-35deg)"></div>

<!-- CAMP BAND -->
<div class="photo band" style="top:1360px;height:482px;background:radial-gradient(ellipse 220px 180px at 560px 170px,rgba(168,124,70,.85) 0%,rgba(120,88,52,.4) 55%,rgba(0,0,0,0) 80%),radial-gradient(ellipse 200px 170px at 780px 140px,rgba(150,106,60,.85) 0%,rgba(0,0,0,0) 80%),linear-gradient(180deg,#3e3226 0%,#5b4a36 40%,#6e5a3c 70%,#4a3d2b 100%)" role="img" aria-label="Two male lions walking through savanna grass"></div>
<div class="frame" style="top:1442px;height:320px"></div>
<h2 class="abs band-title" style="left:250px;top:1506px">Tolvi Camp</h2>
<div class="abs band-sub" style="left:254px;top:1552px">YOUR WILDLIFE DESTINATION</div>
<p class="abs band-text" style="left:250px;top:1578px">Et harum quidem rerum facilis est et expedita distinctio. Nam libero tempore, cum soluta nobis est eligendi optio cumque nihil impedit quo minus id quod maxime placeat facere possimus, omnis voluptas assumenda est, omnis dolor repellendus. Temporibus autem quibusdam et aut officiis debitis aut rerum necessitatibus saepe eveniet ut et voluptates repudiandae sint et molestiae non recusandae. Itaque earum rerum hic tenetur a sapiente delectus, ut aut reiciendis voluptatibus maiores alias consequatur aut perferendis doloribus asperiores repellat</p>
<div class="abs band-link" style="left:250px;top:1692px">READ MORE ABOUT CAMP &nbsp;<b>→</b></div>
<div class="abs corner-mark" style="left:960px;top:1712px"><span class="c"></span>Tolvi Camp</div>

<!-- DESTINATIONS -->
<div class="abs sec-mark" style="top:1866px"><span class="c"></span>Tolvi Camp</div>
<h2 class="abs sec-title" style="top:1956px">Popular Destinations</h2>
<div class="abs sec-sub" style="top:2010px">VIEW ALL DESTINATIONS</div>

<div class="tile" style="left:154px;top:2062px"><div class="pic" style="background:radial-gradient(ellipse 90px 60px at 50% 62%,#4a6a7a 0%,#3a4a4a 50%,rgba(0,0,0,0) 85%),linear-gradient(180deg,#c4ccd0 0%,#b4b6a8 40%,#8a7c5c 70%,#6e6048)" role="img" aria-label="Safari jeep with tourists on the plains"></div><div class="cap"><p>AT VERO EOS ET ACCUSAMUS</p><small>VIEW TOUR PLAN</small></div></div>
<div class="tile" style="left:384px;top:2062px"><div class="pic" style="background:radial-gradient(ellipse 80px 70px at 40% 55%,#8a6a44 0%,rgba(0,0,0,0) 80%),radial-gradient(ellipse 70px 70px at 65% 45%,#6a5036 0%,rgba(0,0,0,0) 80%),linear-gradient(180deg,#2e3430,#3e3e34 60%,#5a4a34)" role="img" aria-label="Two lions resting together"></div><div class="cap"><p>AT VERO EOS ET ACCUSAMUS</p><small>VIEW TOUR PLAN</small></div></div>
<div class="tile" style="left:614px;top:2062px"><div class="pic" style="background:radial-gradient(ellipse 40px 50px at 58% 32%,#d6a02e 0%,#5a4a2a 60%,rgba(0,0,0,0) 85%),linear-gradient(180deg,#d6d8cc 0%,#c4c6b4 45%,#4e5a32 70%,#8a7e52)" role="img" aria-label="Hot air balloon over acacia trees"></div><div class="cap"><p>AT VERO EOS ET ACCUSAMUS</p><small>VIEW TOUR PLAN</small></div></div>
<div class="tile" style="left:844px;top:2062px"><div class="pic" style="background:radial-gradient(ellipse 80px 90px at 50% 50%,#6a625a 0%,#4e4840 50%,rgba(0,0,0,0) 85%),linear-gradient(180deg,#c8a070 0%,#8a7254 45%,#5a4e3e)" role="img" aria-label="African elephant in the bush"></div><div class="cap"><p>AT VERO EOS ET ACCUSAMUS</p><small>VIEW TOUR PLAN</small></div></div>
<div class="tile" style="left:154px;top:2338px"><div class="pic" style="background:radial-gradient(ellipse 60px 90px at 55% 50%,#c8a468 0%,#a4844e 50%,rgba(0,0,0,0) 85%),linear-gradient(180deg,#8e927a,#7a7a5a 50%,#a89060)" role="img" aria-label="Cheetah sitting in grass"></div><div class="cap"><p>AT VERO EOS ET ACCUSAMUS</p><small>VIEW TOUR PLAN</small></div></div>
<div class="tile" style="left:384px;top:2338px"><div class="pic" style="background:radial-gradient(ellipse 80px 50px at 60% 55%,#2a2a2a 0%,#4a4240 50%,rgba(0,0,0,0) 85%),linear-gradient(180deg,#d8dcde 0%,#cfc4b4 35%,#d08a4a 65%,#b46a34)" role="img" aria-label="Photographer with a telephoto lens"></div><div class="cap"><p>AT VERO EOS ET ACCUSAMUS</p><small>VIEW TOUR PLAN</small></div></div>
<div class="tile" style="left:614px;top:2338px"><div class="pic" style="background:radial-gradient(ellipse 50px 60px at 48% 45%,#d46a2a 0%,#2a70b8 45%,rgba(0,0,0,0) 85%),linear-gradient(180deg,#5c6a4c,#3a4a2e 60%,#2a3420)" role="img" aria-label="Kingfisher perched on a branch"></div><div class="cap"><p>AT VERO EOS ET ACCUSAMUS</p><small>VIEW TOUR PLAN</small></div></div>
<div class="tile" style="left:844px;top:2338px"><div class="pic" style="background:radial-gradient(ellipse 50px 110px at 45% 50%,#b48a54 0%,#8a6c44 50%,rgba(0,0,0,0) 85%),linear-gradient(180deg,#a4acb0 0%,#9a9c94 55%,#8a7a5a)" role="img" aria-label="Giraffe with calf"></div><div class="cap"><p>AT VERO EOS ET ACCUSAMUS</p><small>VIEW TOUR PLAN</small></div></div>

<!-- HIGHLIGHTS -->
<div class="photo band" style="top:2640px;height:346px;background:radial-gradient(ellipse 120px 200px at 540px 300px,rgba(40,32,24,.8) 0%,rgba(0,0,0,0) 80%),radial-gradient(ellipse at 30% 60%,#5a4c3c 0%,rgba(0,0,0,0) 60%),linear-gradient(90deg,#3a322a,#4e4234 50%,#3a3128)" role="img" aria-label="Bird perched on a dead branch in soft light"></div>
<h2 class="abs hl-title" style="top:2736px">TRAVELING HIGHLIGHTS</h2>
<div class="abs hl-sub" style="top:2794px">YOUR NEW TRAVELING IDEA</div>
<div class="abs ring"><svg width="18" height="20"><path d="M3 2 L16 10 L3 18Z" fill="none" stroke="#fff" stroke-width="2.5"/></svg></div>

<!-- PACKAGES -->
<div class="abs sec-mark" style="top:3018px"><span class="c"></span>Tolvi Camp</div>
<h2 class="abs pkg-title" style="top:3118px">TOP &amp; POPULAR PACKAGES</h2>
<div class="abs sec-sub" style="top:3170px">VIEW ALL PACKAGES</div>

<div class="card" style="left:154px"><div class="img" style="background:radial-gradient(ellipse 70px 120px at 55% 45%,#8a9098 0%,#5a6068 50%,rgba(0,0,0,0) 85%),linear-gradient(180deg,#5a6a58 0%,#3e5058 50%,#4a6a7a 80%,#2e3a3e)" role="img" aria-label="Grey crowned crane by the water"></div><h3>Kenya and South Africa - Wildlife Special</h3><p>Temporibus autem quibusdam et aut officiis debitis aut rerum necessitatibus saepe eveniet</p><div class="meta">⧗ 4 Days/ 3 Night &nbsp;|&nbsp; From 65 €</div><div class="btn-dark">READ MORE →</div></div>
<div class="card" style="left:456px"><div class="img" style="background:radial-gradient(ellipse 70px 140px at 50% 50%,#9a9a9a 0%,#6a6a6a 50%,rgba(0,0,0,0) 85%),linear-gradient(180deg,#5a5a5a 0%,#b4b4b4 40%,#d0d0d0 70%,#6a6a6a)" role="img" aria-label="Black and white giraffe running"></div><h3>Kenya and South Africa - Wildlife Special</h3><p>Temporibus autem quibusdam et aut officiis debitis aut rerum necessitatibus saepe eveniet</p><div class="meta">⧗ 4 Days/ 3 Night &nbsp;|&nbsp; From 65 €</div><div class="btn-dark">READ MORE →</div></div>
<div class="card" style="left:766px"><div class="img" style="background:radial-gradient(ellipse 100px 120px at 50% 45%,#b07a3e 0%,#7a5028 50%,rgba(0,0,0,0) 85%),linear-gradient(180deg,#2e2014,#3d2a1a 60%,#5a4a2a)" role="img" aria-label="Male lion walking toward the camera"></div><h3>Kenya and South Africa - Wildlife Special</h3><p>Temporibus autem quibusdam et aut officiis debitis aut rerum necessitatibus saepe eveniet</p><div class="meta">⧗ 4 Days/ 3 Night &nbsp;|&nbsp; From 65 €</div><div class="btn-dark">READ MORE →</div></div>

<!-- TESTIMONIAL -->
<div class="photo band" style="top:3824px;height:478px;background:radial-gradient(ellipse 220px 300px at 1050px 120px,rgba(40,48,30,.85) 0%,rgba(0,0,0,0) 80%),radial-gradient(ellipse 200px 200px at 40px 60px,rgba(40,48,30,.75) 0%,rgba(0,0,0,0) 80%),linear-gradient(180deg,#4a5a66 0%,#6a808e 35%,#4e6878 55%,#8a7860 70%,#5a4a38 85%,#3a2e22)" role="img" aria-label="Beach with lounge chairs and palm trees at dusk"></div>
<div class="frame" style="top:3904px;height:326px"></div>
<h2 class="abs band-title" style="left:250px;top:3940px">What Our guests say</h2>
<div class="abs band-sub" style="left:254px;top:3986px">YOUR WILDLIFE DESTINATION</div>
<p class="abs band-text" style="left:250px;top:4010px">Et harum quidem rerum facilis est et expedita distinctio. Nam libero tempore, cum soluta nobis est eligendi optio cumque nihil impedit quo minus id quod maxime placeat facere possimus, omnis voluptas assumenda est, omnis dolor repellendus. Temporibus autem quibusdam et aut officiis debitis aut rerum necessitatibus saepe eveniet ut et voluptates repudiandae sint et molestiae non recusandae. Itaque earum rerum hic tenetur a sapiente delectus, ut aut reiciendis voluptatibus maiores alias consequatur aut perferendis doloribus asperiores repellat</p>
<div class="abs" style="left:250px;top:4124px;color:var(--gold);font-size:13px;letter-spacing:1px">★★★★★</div>
<div class="abs band-link" style="left:250px;top:4144px;letter-spacing:1px">MIRA K. ODHIAMBO</div>
<div class="abs" style="left:250px;top:4160px;font-size:7px;font-weight:700;letter-spacing:1px;color:#fff">VERIFIED CUSTOMER</div>
<div class="abs" style="left:902px;top:4226px;color:var(--accent);font-size:14px">← →</div>
<div class="abs corner-mark" style="left:960px;top:4168px"><span class="c"></span>Tolvi Camp</div>

<!-- PARTNERS -->
<h2 class="abs partner-title">OUR PARTNER</h2>
<div class="partner" style="left:154px">Savanna Routes</div>
<div class="partner" style="left:334px;color:#e08a12">Kora Trails</div>
<div class="partner" style="left:514px;color:#1a3a6a">Plainsway</div>
<div class="partner" style="left:694px;color:#444">Acacia Co</div>
<div class="partner" style="left:874px;color:#1a8fb0">Rift Journeys</div>

<!-- FOOTER -->
<div class="abs footer" role="img" aria-label="Savanna sunset with silhouetted antelope and acacia trees"></div>
<svg class="abs" style="left:0;top:4600px" width="1200" height="60" viewBox="0 0 1200 60" preserveAspectRatio="none"><path d="M0 0 L1200 0 L1200 30 C 900 0, 700 50, 500 30 S 150 10, 0 40Z" fill="#f3f4f7"/></svg>
<div class="abs brand" style="left:530px;top:4720px;font-size:17px"><span class="dot" style="width:40px;height:40px"></span>Tolvi Camp</div>

<div class="abs f-small" style="left:156px;top:4860px">SUBSCRIBE OUR</div>
<div class="abs f-big" style="left:156px;top:4874px">NEWSLETTER</div>
<div class="abs" style="left:156px;top:4900px;width:226px;height:32px;background:#fff;font-size:8px;color:#aaa;padding:12px 14px">ENTER YOUR EMAIL ID</div>
<div class="abs" style="left:382px;top:4900px;width:38px;height:32px;background:var(--blue);display:flex;align-items:center;justify-content:center"><svg width="14" height="14"><path d="M1 7 L13 1 L9 13 L7 8Z" fill="#fff"/></svg></div>
<div class="abs" style="left:156px;top:4950px;width:10px;height:10px;background:#fff"></div>
<div class="abs" style="left:170px;top:4948px;font-size:8.5px;line-height:17px;color:#fff;width:220px">I agree to my email being stored and used to receive the newsletter</div>
<div class="abs" style="left:156px;top:4990px;width:132px;height:30px;background:var(--red);color:#fff;font-size:12px;display:flex;align-items:center;justify-content:center">SUBSCRIBE</div>

<div class="abs f-small" style="left:516px;top:4862px">QUICK</div>
<div class="abs f-big" style="left:516px;top:4876px">LINKS</div>
<div class="abs f-links">HOME<br>ACTIVITIES<br>ACCOMMODATION<br>ITINERARIES<br>GALLERIES<br>MORE INFO</div>

<div class="abs f-small" style="left:756px;top:4862px">SCHEDULE</div>
<div class="abs f-big" style="left:756px;top:4876px">CONSULTATION</div>
<div class="abs f-info" style="top:4910px">info@tolvicamp.com</div>
<div class="abs f-info" style="top:4930px">000-418-2290 &nbsp;/&nbsp; 030-552-1700</div>
<div class="abs social"><span aria-label="Social link 1"></span><span aria-label="Social link 2"></span><span aria-label="Social link 3"></span></div>

<div class="abs copy">Copyright © 2023 Tolvi Camp - Masai Mara &nbsp;|&nbsp; All Rights Reserved.</div>

</body>
</html>
```